Keto Food Brand Needs Packaging Design and Logo

We need a logo and packaging design for a stand-up food bag for our keto shake mix. We are a health and wellness brand launching our first shake mix product. I would like bold, bright colors. This document goes more in depth . This brand might encompass more than only food so I want the logo to be versatile for supplements and other health products. https://files.quarnix-docs.example/share/8hTzq3PmVx41KdLw92RaYcbE07nGsJuQfM5oXt2iHkAp/view?mode=sharing See images of logos attached. It doesn't have to be food for the logo but I like the creativity of the ones listed.

Target Market(s)

Keto. Health and Fitness

Logo Text

Trevalo

Font styles to use
Serif
Sans Serif

Colors

Designer to choose colors to be used in the design.

```html
<!DOCTYPE html>
<html lang="en">
<head>
<meta charset="utf-8">
<title>Trevalo Keto Shake Mix – Pouch Front</title>
<link rel="stylesheet" href="https://fonts.googleapis.com/css2?family=Poppins:wght@400;500;600&display=swap">
<style>
  :root {
    --bg: #7ed6c8;
    --pouch: #f4f4f2;
    --pouch-shade: #e3e3e0;
    --red: #e4434b;
    --orange: #f08a1c;
    --orange-deep: #e0601d;
    --brand: #e2541f;
    --label-ink: #b4521a;
    --rule: #f08a1c;
    --tab-line: #9a6a4a;
    --white: #ffffff;
  }
  * { margin: 0; padding: 0; box-sizing: border-box; }
  html, body { width: 1200px; height: 987px; overflow: hidden; }
  body { background: var(--bg); font-family: "Poppins", sans-serif; }

  .pouch {
    position: absolute;
    left: 405px; top: 170px;
    width: 390px; height: 640px;
    background: linear-gradient(180deg, var(--pouch) 0%, var(--white) 40%, var(--pouch-shade) 100%);
    border-radius: 6px;
    box-shadow: 0 30px 60px rgba(20, 80, 70, 0.25);
  }
  .pouch__zipper {
    position: absolute; left: 0; right: 0; top: 46px;
    height: 2px; background: var(--pouch-shade);
  }
  .pouch__notch {
    position: absolute; top: 70px; width: 8px; height: 8px;
    border-radius: 50%; background: var(--pouch-shade);
  }
  .pouch__notch--left { left: 12px; }
  .pouch__notch--right { right: 12px; }

  .panel {
    position: absolute;
    left: 38px; right: 32px; top: 96px; bottom: 66px;
    background: linear-gradient(90deg, var(--red) 0%, var(--red) 9%, var(--orange-deep) 22%, var(--orange) 75%, var(--orange-deep) 100%);
    overflow: hidden;
  }

  .logo-tab {
    position: absolute;
    left: 62px; width: 196px; top: -2px; height: 156px;
    background: var(--white);
    border: 1.5px solid var(--tab-line);
    border-top: none;
    border-radius: 0 0 22px 22px;
    display: flex; align-items: center; justify-content: center; gap: 8px;
  }
  .logo-tab__dot {
    width: 12px; height: 12px; border-radius: 50%; background: var(--brand);
  }
  .logo-tab__name {
    font-weight: 600; font-size: 34px; color: var(--brand); letter-spacing: 0.5px;
  }

  .nutrition {
    position: absolute; left: 70px; top: 168px;
    font-size: 10.5px; font-weight: 500; color: var(--white);
    padding-bottom: 4px; border-bottom: 1px solid rgba(255,255,255,0.8);
    white-space: nowrap;
  }

  .illustration {
    position: absolute; left: 60px; right: 0; top: 212px; height: 200px;
    background: radial-gradient(ellipse at 30% 40%, rgba(255, 205, 90, 0.65) 0%, rgba(255, 190, 70, 0.2) 45%, transparent 70%),
                radial-gradient(ellipse at 78% 78%, rgba(140, 85, 45, 0.85) 0%, rgba(150, 95, 50, 0.5) 30%, transparent 55%);
  }

  .ingredients {
    position: absolute; left: 30px; bottom: 0;
    width: 160px; height: 150px;
    background: var(--white);
    border-radius: 22px 22px 0 0;
    padding: 22px 18px 0 18px;
    list-style: none;
  }
  .ingredients__item {
    font-size: 10.5px; font-weight: 500; color: var(--label-ink);
    padding-bottom: 4px; margin-bottom: 12px;
    border-bottom: 1.5px solid var(--rule);
    width: 100px; white-space: nowrap;
  }
  .ingredients__item--wide { width: 124px; }
</style>
</head>
<body>
  <div class="pouch">
    <div class="pouch__zipper"></div>
    <span class="pouch__notch pouch__notch--left"></span>
    <span class="pouch__notch pouch__notch--right"></span>

    <div class="panel">
      <div class="logo-tab">
        <span class="logo-tab__dot"></span>
        <span class="logo-tab__name">Trevalo</span>
      </div>

      <p class="nutrition">15g FAT - 0g - SUGAR - 1g NET CARBS</p>

      <div class="illustration" role="img" aria-label="Golden leafy branch illustration with whole almonds"></div>

      <ul class="ingredients">
        <li class="ingredients__item">+100% CACAO</li>
        <li class="ingredients__item ingredients__item--wide">+COCONUT BUTTER</li>
        <li class="ingredients__item">+MCT OIL</li>
      </ul>
    </div>
  </div>
</body>
</html>
```